Web Design

We are Carvento’s new and used car supermarket, we need a clean and nice look web design.

What included on homepage:
1. Logo
2. Slideshow (additional)
3. Menu - Home, About us, New cars, Used cars, Contact us
4. Advance Search
5. Customer Reviews
6. Social links - facebook, twitter , youtube
7. Banner Ads
8. Recent News
9. Newsletter

We just need psd files, home and contact us.

Industry/Entity Type

Used Car

Number of Pages Required

2 page

Requirements
Must have
• Webpage are well designed and in accordance with the color of the logo that is displayed in the file attachment.

```html
<!DOCTYPE html>
<html lang="en">
<head>
<meta charset="utf-8">
<title>Carvento's Car Supermarket</title>
<link href="https://fonts.googleapis.com/css2?family=Ubuntu:ital,wght@0,400;0,500;0,700;1,400;1,500&family=Lora:ital@1&display=swap" rel="stylesheet">
<style>
:root{
  --blue:#0b5aa6;
  --blue-dark:#074487;
  --blue-deep:#063f86;
  --red:#d8152a;
  --page:#eeeff1;
  --panel:#f4f4f5;
  --line:#cfd3d8;
  --text:#555a60;
  --white:#ffffff;
}
*{box-sizing:border-box;margin:0;padding:0}
html,body{width:958px;height:1200px;overflow:hidden}
body{position:relative;background:var(--page);font-family:'Ubuntu',sans-serif;color:var(--text)}
.abs{position:absolute}
.top-bar{left:0;top:0;width:958px;height:6px;background:var(--blue)}

/* header */
.brand{left:102px;top:60px;display:flex;align-items:center;gap:9px}
.brand-mark{width:14px;height:14px;background:var(--blue)}
.brand-name{font-weight:500;font-size:28px;color:var(--blue);line-height:32px}
.main-nav{left:468px;top:54px;width:386px;height:46px}
.main-nav svg{position:absolute;left:0;top:0}
.main-nav ul{position:absolute;left:24px;top:0;height:46px;display:flex;gap:17px;align-items:center;list-style:none}
.main-nav li{color:var(--white);font-size:12.3px;text-transform:uppercase}

/* slider */
.slider{left:102px;top:141px;width:496px;height:293px;border-radius:3px;overflow:hidden;
  background:radial-gradient(ellipse at 50% 60%,#e9e4da 0%,#b9ab95 45%,#6d5e4c 100%)}
.slide-caption{left:0;top:17px;height:31px;width:256px;background:rgba(40,34,28,.82);color:var(--white);
  font-size:14.5px;line-height:31px;padding-left:7px;clip-path:polygon(0 0,92% 0,100% 100%,0 100%)}
.slide-arrow{top:100px}
.slide-dots{left:224px;top:278px;display:flex;gap:5px}
.slide-dots span{width:8px;height:8px;border-radius:50%;background:#d8d8d8}
.slide-dots span.on{background:var(--red)}

/* search */
.search{left:614px;top:141px;width:240px;height:144px;border-radius:3px;background:linear-gradient(#1b72c4,#0b5aa6 60%,#0a4f98)}
.search h3{height:30px;line-height:30px;padding-left:17px;color:var(--white);font-weight:500;font-size:13.5px;text-transform:uppercase;background:var(--blue-dark);border-radius:3px 3px 0 0}
.select{left:17px;width:195px;height:24px;background:var(--white);border-radius:2px;font-family:'Lora',serif;font-style:italic;font-size:8px;color:#777;line-height:24px;padding-left:10px}
.select::after{content:"";position:absolute;right:8px;top:10px;border:4px solid transparent;border-top:5px solid #333;border-bottom:none}
.btn-search{left:17px;top:109px;width:47px;height:20px;border-radius:3px;background:var(--red);border:1.5px solid #f1b9bf;color:var(--white);font-size:6.5px;font-weight:500;text-align:center;line-height:17px}

/* social */
.connect{left:614px;top:291px;width:240px;height:143px;border:1px solid var(--line);border-radius:3px;background:linear-gradient(#fbfbfb,#eeeeee)}
.connect h3{text-align:center;margin-top:23px;color:var(--blue);font-weight:500;font-size:16.5px;text-transform:uppercase}
.social{left:12px;top:66px;display:flex;gap:14px}
.social span{width:42px;height:42px;border-radius:50%;border:1.5px solid;background:var(--white)}

/* welcome */
.welcome{left:102px;top:472px;width:480px}
.welcome h1{font-weight:500;font-size:19.2px;color:var(--blue);text-transform:uppercase;white-space:nowrap}
.welcome p{font-size:10.6px;line-height:13.7px;margin-top:9px;letter-spacing:.15px}
.welcome p+p{margin-top:13px}

.reviews-title{left:102px;top:636px;font-size:18.5px;font-weight:500;color:var(--blue)}
.reviews-title em{font-style:italic}
.review-dots{left:551px;top:644px;display:flex;gap:3px}
.review-dots span{width:4.5px;height:4.5px;border-radius:50%;background:#aab0b6}
.review-dots span.on{background:var(--blue)}
.review{top:694px;width:151px}
.review .bubble{height:58px;background:var(--panel);border:1px solid #e1e3e5;border-bottom:2px solid var(--blue);border-radius:4px;padding:10px 12px 0 22px;
  font-family:'Lora',serif;font-style:italic;font-size:6.2px;line-height:10px;color:#8d9196;position:relative}
.review .bubble b{position:absolute;left:8px;top:7px;color:var(--red);font-size:12px;font-family:'Lora',serif;font-style:normal}
.review .tail{position:absolute;left:20px;top:56px}
.review .who{display:flex;align-items:center;gap:7px;margin:10px 0 0 15px;font-size:6px;color:var(--blue)}
.review .who i{width:18px;height:18px;border-radius:50%;background:linear-gradient(#d9c4b5,#8a6e5d);border:1px solid #e5e5e5}

.banner-ad{left:614px;top:476px;width:240px;height:336px;background:#e0e0e0;border:2px solid #c5c7ca;border-radius:2px;
  text-align:center;color:#7a7c80;font-weight:500;font-size:23px;line-height:37px;padding-top:25px;text-transform:uppercase}

/* lower */
.lower{left:0;top:839px;width:958px;height:301px;background:var(--white)}
.col-title{top:859px;font-size:19.5px;font-weight:400;color:var(--blue)}
.v-rule{top:900px;width:1px;height:190px;background:#d7dadd}
.news{left:103px;width:198px}
.news .date{position:absolute;left:0;top:0;width:32px;border-radius:2px;overflow:hidden;text-align:center;background:#e7e9ec;border:1px solid #d5d8dc}
.news .date b{display:block;background:var(--blue);color:var(--white);font-size:7.5px;font-weight:400;line-height:10px}
.news .date span{display:block;font-size:12px;color:var(--blue-dark);line-height:18px}
.news h4{margin-left:45px;font-weight:500;font-size:10.8px;color:var(--blue)}
.news p{margin:4px 0 0 45px;width:132px;font-size:5.6px;line-height:8.8px;color:#666}
.news p a{color:var(--blue)}
.news-rule{left:103px;width:198px;height:1px;background:#d7dadd}
.gallery-main{left:386px;top:906px;width:231px;height:112px;border:2px solid #dcdfe2;background:var(--white);padding:5px}
.gallery-main div,.thumb div{width:100%;height:100%;background:radial-gradient(ellipse at 50% 55%,#e6323a 0%,#c61a24 38%,#f1f1f1 62%,#fff 100%)}
.thumb{top:1038px;height:44px;border:1px solid #cfd3d7;background:var(--white);padding:4px}
.thumb.on{border:2px solid var(--blue)}
.thumb-pointer{left:413px;top:1030px}
.newsletter-text{left:688px;top:921px;font-size:10.2px;line-height:14.5px;color:#444}
.email{left:686px;top:957px;width:167px;height:24px;border:1.5px solid #b9bec4;border-radius:3px;background:var(--white);
  font-family:'Lora',serif;font-style:italic;font-size:8px;color:#999;line-height:21px;padding-left:19px}
.subscribe{left:690px;top:1003px;width:137px;height:34px;border-radius:3px;background:linear-gradient(#1b6cba,#0a4a8f);color:var(--white);font-size:17.5px;font-weight:500;text-align:center;line-height:34px}

.footer{left:0;top:1140px;width:958px;height:60px;background:var(--blue-deep)}
.footer ul{position:absolute;left:102px;top:0;height:60px;display:flex;align-items:center;gap:17px;list-style:none}
.footer li{color:var(--white);font-size:11.8px}
.footer small{position:absolute;right:105px;top:23px;color:var(--white);font-size:9.3px}
</style>
</head>
<body>
<div class="abs top-bar"></div>

<header>
  <div class="abs brand">
    <span class="brand-mark"></span>
    <span class="brand-name">Carvento</span>
  </div>
  <nav class="abs main-nav">
    <svg width="386" height="46" viewBox="0 0 386 46"><polygon points="14,0 386,0 386,46 0,46" fill="#d8152a"/><polygon points="14,0 386,0 386,3 13,3" fill="#ee3a4b"/></svg>
    <ul><li>Home</li><li>About us</li><li>New cars</li><li>Used cars</li><li>Contact us</li></ul>
  </nav>
</header>

<section class="abs slider" role="img" aria-label="Slideshow photo of a white sports coupe parked in a sepia-toned plaza">
  <div class="abs slide-caption">LOREM IPSUM DUMMY TEXT</div>
  <svg class="abs slide-arrow" style="left:6px" width="18" height="30" viewBox="0 0 18 30"><polyline points="15,3 4,15 15,27" fill="none" stroke="#8a8a8a" stroke-width="5" opacity=".7"/></svg>
  <svg class="abs slide-arrow" style="left:472px" width="18" height="30" viewBox="0 0 18 30"><polyline points="3,3 14,15 3,27" fill="none" stroke="#8a8a8a" stroke-width="5" opacity=".7"/></svg>
  <div class="abs slide-dots"><span></span><span class="on"></span><span></span><span></span></div>
</section>

<aside class="abs search">
  <h3>Search Cars</h3>
  <div class="abs select" style="top:45px">Select model</div>
  <div class="abs select" style="top:76px">Select manufacturer</div>
  <div class="abs btn-search">Search Now</div>
</aside>

<aside class="abs connect">
  <h3>Keep Connected</h3>
  <div class="abs social">
    <span style="border-color:#3b5a9a" role="img" aria-label="Social network link"></span>
    <span style="border-color:#2aa3d8" role="img" aria-label="Social network link"></span>
    <span style="border-color:#d8152a" role="img" aria-label="Video channel link"></span>
    <span style="border-color:#f26a1b" role="img" aria-label="News feed link"></span>
  </div>
</aside>

<section class="abs welcome">
  <h1>Welcome to Carvento's Car Supermarket</h1>
  <p>Lorem ipsum dolor sit amet, consectetur adipisicing elit, sed do eiusmod tempor incididunt ut labore et dolore magna aliqua. Ut enim ad minim veniam, quis nostrud exercitation ullamco laboris nisi ut aliquip ex ea commodo consequat.</p>
  <p>Duis aute irure dolor in reprehenderit in voluptate velit esse cillum dolore eu fugiat nulla pariatur. Excepteur sint occaecat cupidatat non proident, sunt in culpa qui officia deserunt mollit anim id est laborum.</p>
</section>

<h2 class="abs reviews-title">What our customers <em>SAY</em></h2>
<div class="abs review-dots"><span></span><span class="on"></span><span></span><span></span></div>

<div class="abs review" style="left:102px">
  <div class="bubble"><b>&ldquo;</b>Lorem ipsum dolor sit amet, consec tetur adipisicing elit, sed do eiusmod tempor incididunt ut labore.
    <svg class="tail" width="16" height="11" viewBox="0 0 16 11"><polygon points="0,0 16,0 8,10" fill="#f4f4f5"/><polyline points="0,1 8,10 16,1" fill="none" stroke="#0b5aa6" stroke-width="1.5"/></svg></div>
  <div class="who"><i role="img" aria-label="Customer portrait"></i>Dan Mercer, Portland</div>
</div>
<div class="abs review" style="left:273px">
  <div class="bubble"><b>&ldquo;</b>Lorem ipsum dolor sit amet, consec tetur adipisicing elit, sed do eiusmod tempor incididunt ut labore.
    <svg class="tail" width="16" height="11" viewBox="0 0 16 11"><polygon points="0,0 16,0 8,10" fill="#f4f4f5"/><polyline points="0,1 8,10 16,1" fill="none" stroke="#0b5aa6" stroke-width="1.5"/></svg></div>
  <div class="who"><i role="img" aria-label="Customer portrait"></i>Dan Mercer, Portland</div>
</div>
<div class="abs review" style="left:443px">
  <div class="bubble"><b>&ldquo;</b>Lorem ipsum dolor sit amet, consec tetur adipisicing elit, sed do eiusmod tempor incididunt ut labore.
    <svg class="tail" width="16" height="11" viewBox="0 0 16 11"><polygon points="0,0 16,0 8,10" fill="#f4f4f5"/><polyline points="0,1 8,10 16,1" fill="none" stroke="#0b5aa6" stroke-width="1.5"/></svg></div>
  <div class="who"><i role="img" aria-label="Customer portrait"></i>Dan Mercer, Portland</div>
</div>

<div class="abs banner-ad">Put your banner<br>ad here</div>

<section class="abs lower"></section>

<h2 class="abs col-title" style="left:102px">Recent News</h2>
<h2 class="abs col-title" style="left:384px">Gallery</h2>
<h2 class="abs col-title" style="left:686px;top:858px">Newsletter</h2>
<div class="abs v-rule" style="left:343px"></div>
<div class="abs v-rule" style="left:651px"></div>

<article class="abs news" style="top:908px">
  <div class="date"><b>Aug</b><span>15</span></div>
  <h4>Adipisicing elit sed</h4>
  <p>Eiusmod tempor incididunt ut labore et dolore magna aliqua. Ut enim ad minim veniam, quis nostrud exercitation ullam...<a>[Read More]</a></p>
</article>
<div class="abs news-rule" style="top:965px"></div>
<article class="abs news" style="top:980px">
  <div class="date"><b>Aug</b><span>15</span></div>
  <h4>Adipisicing elit sed</h4>
  <p>Eiusmod tempor incididunt ut labore et dolore magna aliqua. Ut enim ad minim veniam, quis nostrud exercitation ullam...<a>[Read More]</a></p>
</article>
<div class="abs news-rule" style="top:1043px"></div>
<article class="abs news" style="top:1058px">
  <div class="date"><b>Aug</b><span>15</span></div>
  <h4>Adipisicing elit sed</h4>
  <p>Eiusmod tempor incididunt ut labore et dolore magna aliqua. Ut enim ad minim veniam, quis nostrud exercitation ullam...<a>[Read More]</a></p>
</article>

<div class="abs gallery-main"><div role="img" aria-label="Photo of a red sports car with white racing stripes"></div></div>
<svg class="abs thumb-pointer" width="16" height="9" viewBox="0 0 16 9"><polygon points="0,9 8,0 16,9" fill="#0b5aa6"/></svg>
<div class="abs thumb on" style="left:387px;width:68px"><div role="img" aria-label="Thumbnail of a red sports car"></div></div>
<div class="abs thumb" style="left:468px;width:64px"><div style="background:radial-gradient(ellipse,#b9bcc4 0%,#8e929c 40%,#fff 66%)" role="img" aria-label="Thumbnail of a silver coupe"></div></div>
<div class="abs thumb" style="left:546px;width:64px"><div style="background:radial-gradient(ellipse,#2f6fd0 0%,#163f8c 40%,#fff 66%)" role="img" aria-label="Thumbnail of a blue sports car"></div></div>

<p class="abs newsletter-text">Sign up to receive daily updates<br>and news from Carvento's</p>
<div class="abs email">Enter your Email</div>
<div class="abs subscribe">Subscribe</div>

<footer class="abs footer">
  <ul><li>Home</li><li>About us</li><li>New cars</li><li>Used cars</li><li>Contact us</li></ul>
  <small>Copyright&copy;carventocarsupermarket2014. All Rights Reserved</small>
</footer>
</body>
</html>
```